Patient Engagement Solution

We need an attractive and easy-to-use GUI for patients and clinicians, which includes screens and icons. The application has been named Quorvix. I have our corporate logo attached as well.
I have attached the screens that the developer has used to create the solution, but we all know they miss the target when it comes to the creative stuff.
If it helps, I can supply some competitor's screens as a guide - please let me know.

Target Market(s)

Patients and Clinicians

Industry/Entity Type

Healthcare/Hospitals

Font styles to use
Other font styles liked:
• Easy to Read

Requirements
Must have
• Attractive, easy to use graphical user interface. Screen size is usually 22" 16:9
Nice to have
• Inviting and interesting look
Should not have
• Complicated hard to navigate screens

```html
<!DOCTYPE html>
<html lang="en">
<head>
<meta charset="utf-8">
<title>Quorvix – Patient Engagement Screens</title>
<link rel="stylesheet" href="https://fonts.googleapis.com/css2?family=Montserrat:wght@400;500;600;700&display=swap">
<style>
  :root {
    --page: #1a1a1a;
    --screen-light: #d8dbdf;
    --screen-mid: #c2c6cb;
    --tile: rgba(255,255,255,0.93);
    --ink: #2a2a2a;
    --icon-dark: #1c0303;
    --accent: #c4161c;
    --white: #ffffff;
  }
  * { box-sizing: border-box; margin: 0; padding: 0; }
  html, body { width: 790px; height: 1200px; overflow: hidden; }
  body {
    background: var(--page);
    font-family: "Montserrat", sans-serif;
    color: var(--ink);
    position: relative;
  }
  .screen {
    position: absolute;
    left: 29px;
    width: 732px;
    height: 366px;
    overflow: hidden;
  }
  .screen--home { top: 30px; }
  .screen--menu { top: 417px; }
  .screen--language { top: 804px; }

  .backdrop-photo {
    position: absolute; inset: 0;
    background: linear-gradient(100deg, var(--screen-mid) 0%, var(--screen-light) 60%, #dde0e4 100%);
  }

  .brand {
    position: absolute;
    left: 0; right: 0; top: 42px;
    text-align: center;
    font-weight: 700;
    font-size: 24px;
    letter-spacing: 0.5px;
    color: var(--icon-dark);
    z-index: 2;
  }
  .brand .dot {
    display: inline-block; width: 7px; height: 7px; border-radius: 50%;
    background: var(--accent); margin-left: 3px; vertical-align: 1px;
  }

  .ward-info { position: absolute; left: 68px; top: 136px; color: var(--white); z-index: 2; }
  .ward-name, .bed-name { font-weight: 700; font-size: 14px; letter-spacing: 0.2px; }
  .clock-time { font-weight: 500; font-size: 50px; line-height: 1; margin: 13px 0 16px -2px; letter-spacing: -1px; }

  .hospital-badge {
    position: absolute; left: 68px; top: 310px; width: 70px; height: 35px;
    background: var(--white); border-radius: 2px; z-index: 2;
    display: flex; align-items: center; justify-content: center; gap: 3px;
    font-size: 6px; font-weight: 600; line-height: 1.15; color: var(--ink);
  }
  .hospital-badge .mark { width: 9px; height: 9px; border-radius: 50%; background: #e0a21f; flex: none; }

  .round-button {
    position: absolute; border-radius: 50%;
    background: rgba(230,232,235,0.75);
    display: flex; align-items: center; justify-content: center; z-index: 2;
  }
  .round-button .core {
    border-radius: 50%; background: var(--white);
    display: flex; align-items: center; justify-content: center;
    box-shadow: 0 2px 8px rgba(0,0,0,0.08);
  }
  .power { left: 317px; top: 232px; width: 98px; height: 98px; }
  .power .core { width: 68px; height: 68px; }
  .home { left: 339px; top: 285px; width: 54px; height: 54px; }
  .home .core { width: 38px; height: 38px; }

  .tile {
    position: absolute; width: 62px; height: 62px;
    background: var(--tile); border-radius: 3px; z-index: 2;
    display: flex; flex-direction: column; align-items: center; justify-content: flex-start;
    padding-top: 13px;
    font-size: 8.5px; font-weight: 500; color: var(--ink);
  }
  .tile svg { width: 22px; height: 20px; margin-bottom: 7px; }
  .tile--caps { font-size: 8px; letter-spacing: 0.3px; text-transform: uppercase; }

  .lang {
    position: absolute; width: 104px; height: 36px;
    background: var(--tile); border-radius: 2px; z-index: 2;
    display: flex; align-items: center; gap: 9px; padding-left: 9px;
    font-size: 8.5px; font-weight: 500;
  }
  .flag {
    width: 23px; height: 23px; border-radius: 50%; flex: none;
    border: 1.5px solid #e6e6e6; position: relative; overflow: hidden;
    display: flex; align-items: center; justify-content: center;
    font-size: 9px; color: #ffd400; line-height: 1;
  }
  .flag--us { background: linear-gradient(#2d3e8c,#2d3e8c) 0 0/50% 50% no-repeat, repeating-linear-gradient(180deg,#d22 0 2.5px,#fff 2.5px 5px); }
  .flag--fr { background: linear-gradient(90deg,#1f3c99 33%,#fff 33% 66%,#e5262e 66%); }
  .flag--ae { background: linear-gradient(90deg,#d21f26 30%,transparent 30%), linear-gradient(180deg,#00843d 33%,#fff 33% 66%,#111 66%); }
  .flag--jp { background: radial-gradient(circle,#d3092d 0 28%,#fff 30%); }
  .flag--it { background: linear-gradient(90deg,#149246 33%,#fff 33% 66%,#ce2b37 66%); }
  .flag--es { background: linear-gradient(180deg,#c60b1e 25%,#ffc400 25% 75%,#c60b1e 75%); }
  .flag--cn, .flag--vn { background: #de2910; }
  .flag--de { background: linear-gradient(180deg,#111 33%,#dd0000 33% 66%,#ffce00 66%); }
  .flag--in { background: radial-gradient(circle,#0a3a8a 0 12%,transparent 14%), linear-gradient(180deg,#ff9933 33%,#fff 33% 66%,#138808 66%); }
  .flag--cn { justify-content: flex-start; align-items: flex-start; padding: 4px 0 0 4px; font-size: 7px; }
</style>
</head>
<body>

<svg width="0" height="0" style="position:absolute">
  <defs>
    <linearGradient id="icon-fill" x1="0" y1="0" x2="1" y2="1">
      <stop offset="0" stop-color="#6a0d0d"/>
      <stop offset="1" stop-color="#140202"/>
    </linearGradient>
  </defs>
</svg>

<!-- Home screen -->
<section class="screen screen--home">
  <div class="backdrop-photo" role="img" aria-label="Background photo of a potted plant against a soft grey wall"></div>
  <div class="brand">Quorvix<span class="dot"></span></div>

  <div class="ward-info">
    <div class="ward-name">DEMO WARD</div>
    <div class="clock-time">15:35</div>
    <div class="bed-name">DEFAULT BED</div>
  </div>

  <div class="hospital-badge"><span class="mark"></span><span>Harbourview<br>Children's<br>Clinic</span></div>

  <div class="round-button power">
    <div class="core">
      <svg width="34" height="34" viewBox="0 0 34 34" fill="none" stroke="#c4161c" stroke-width="3.4" stroke-linecap="round">
        <path d="M10.5 9.5a11 11 0 1 0 13 0"/><path d="M17 4v13"/>
      </svg>
    </div>
  </div>

  <div class="tile tile--caps" style="left:521px;top:82px">
    <svg viewBox="0 0 22 20"><rect x="0" y="1" width="22" height="13" fill="url(#icon-fill)"/><rect x="7" y="16" width="8" height="1.5" fill="#1c0303"/></svg>TV</div>
  <div class="tile tile--caps" style="left:600px;top:82px">
    <svg viewBox="0 0 22 20"><rect x="2" y="4" width="18" height="15" rx="2" fill="url(#icon-fill)"/><path d="M5 4L12 0" stroke="#1c0303" stroke-width="1.5"/><circle cx="8" cy="12" r="3.2" fill="none" stroke="#fff" stroke-width="1.4"/><path d="M13 10h4M13 12.5h4M13 15h4" stroke="#fff" stroke-width="1.2"/></svg>Radio</div>
  <div class="tile tile--caps" style="left:521px;top:157px">
    <svg viewBox="0 0 22 20"><rect x="2" y="0" width="8" height="8" rx="2" fill="url(#icon-fill)"/><rect x="12" y="0" width="8" height="8" rx="2" fill="url(#icon-fill)"/><rect x="2" y="11" width="8" height="8" rx="2" fill="url(#icon-fill)"/><circle cx="16" cy="15" r="4.2" fill="url(#icon-fill)"/></svg>Apps</div>
  <div class="tile tile--caps" style="left:600px;top:157px">
    <svg viewBox="0 0 22 20"><rect x="2" y="0" width="10" height="14" rx="1" fill="url(#icon-fill)"/><rect x="10" y="6" width="10" height="13" rx="1" fill="url(#icon-fill)"/><text x="4" y="10" font-size="8" font-weight="700" fill="#fff" font-family="Montserrat, sans-serif">A</text><path d="M13 10l4 5M17 10l-4 5" stroke="#fff" stroke-width="1.2"/></svg>Language</div>
  <div class="tile tile--caps" style="left:600px;top:230px">
    <svg viewBox="0 0 22 20"><circle cx="11" cy="10" r="9.5" fill="url(#icon-fill)"/><circle cx="11" cy="10" r="6.5" fill="none" stroke="#fff" stroke-width="1.3"/><path d="M8 9l3 3 3-4" fill="none" stroke="#fff" stroke-width="1.4"/></svg>Clock</div>
</section>

<!-- Main menu screen -->
<section class="screen screen--menu">
  <div class="backdrop-photo" role="img" aria-label="Background photo of a potted plant against a soft grey wall"></div>
  <div class="brand">Quorvix<span class="dot"></span></div>

  <div class="tile" style="left:68px;top:124px"><svg viewBox="0 0 22 20"><rect x="0" y="3" width="15" height="14" rx="2" fill="url(#icon-fill)"/><path d="M16 10l6-5v10z" fill="#1c0303"/></svg>Video Call</div>
  <div class="tile" style="left:144px;top:124px"><svg viewBox="0 0 22 20"><path d="M3 11c2-4 5-5 8-4-1 3-4 6-8 4zM11 7c1-4 4-6 8-5 0 4-3 7-7 7zM11 9c3 0 6 2 7 6-4 1-7-1-8-5z" fill="url(#icon-fill)"/><circle cx="8" cy="15" r="3" fill="url(#icon-fill)"/></svg>Relax</div>
  <div class="tile" style="left:220px;top:124px"><svg viewBox="0 0 22 20"><rect x="0" y="1" width="22" height="13" fill="url(#icon-fill)"/><rect x="7" y="16" width="8" height="1.5" fill="#1c0303"/></svg>Clinical</div>
  <div class="tile" style="left:296px;top:124px"><svg viewBox="0 0 22 20"><path d="M11 2L0 7l11 5 11-5z" fill="url(#icon-fill)"/><path d="M4 10v5c4 3 10 3 14 0v-5l-7 3z" fill="url(#icon-fill)"/></svg>Education</div>
  <div class="tile" style="left:372px;top:124px"><svg viewBox="0 0 22 20"><circle cx="11" cy="10" r="7" fill="none" stroke="url(#icon-fill)" stroke-width="5" stroke-dasharray="3.1 2.4"/><circle cx="11" cy="10" r="6" fill="url(#icon-fill)"/><circle cx="11" cy="10" r="2.5" fill="#fff"/></svg>Settings</div>
  <div class="tile" style="left:448px;top:124px"><svg viewBox="0 0 22 20"><path d="M4 1l4 4-2 3c1 3 3 5 6 6l3-2 4 4-3 3C8 19 1 12 1 4z" fill="url(#icon-fill)"/><path d="M12 5a4 4 0 0 1 4 4M12 1a8 8 0 0 1 8 8" fill="none" stroke="#1c0303" stroke-width="1.5"/></svg>Phone</div>
  <div class="tile" style="left:524px;top:124px"><svg viewBox="0 0 22 20"><rect x="0" y="1" width="22" height="13" fill="url(#icon-fill)"/><rect x="7" y="16" width="8" height="1.5" fill="#1c0303"/></svg>Games</div>
  <div class="tile" style="left:600px;top:124px"><svg viewBox="0 0 22 20"><path d="M1 5l18-5 1 3-18 5z" fill="url(#icon-fill)"/><rect x="2" y="8" width="18" height="11" fill="url(#icon-fill)"/><path d="M9 11l5 3-5 3z" fill="#fff"/></svg>Movies</div>

  <div class="tile" style="left:106px;top:199px"><svg viewBox="0 0 22 20"><rect x="2" y="0" width="8" height="8" rx="2" fill="url(#icon-fill)"/><rect x="12" y="0" width="8" height="8" rx="2" fill="url(#icon-fill)"/><rect x="2" y="11" width="8" height="8" rx="2" fill="url(#icon-fill)"/><circle cx="16" cy="15" r="4.2" fill="url(#icon-fill)"/></svg>Apps</div>
  <div class="tile" style="left:182px;top:199px"><svg viewBox="0 0 22 20" fill="none" stroke="#1c0303" stroke-width="2.2" stroke-linecap="round"><path d="M1 7a14 14 0 0 1 20 0"/><path d="M4.5 10.5a9 9 0 0 1 13 0"/><path d="M8 14a4 4 0 0 1 6 0"/><circle cx="11" cy="17.5" r="1" fill="#1c0303"/></svg>Internet</div>
  <div class="tile" style="left:258px;top:199px"><svg viewBox="0 0 22 20"><path d="M1 0v6M3 0v6M5 0v6M3 6v14M20 0v20" stroke="#1c0303" stroke-width="1.4"/><circle cx="12" cy="10" r="6" fill="url(#icon-fill)"/><circle cx="12" cy="10" r="3.5" fill="none" stroke="#fff" stroke-width="1"/></svg>Meal</div>
  <div class="tile" style="left:334px;top:199px"><svg viewBox="0 0 22 20"><path d="M1 2c4-1 7 0 9 2v15c-2-2-5-3-9-2zM21 2c-4-1-7 0-9 2v15c2-2 5-3 9-2z" fill="url(#icon-fill)"/></svg>Books</div>
  <div class="tile" style="left:410px;top:199px"><svg viewBox="0 0 22 20"><path d="M2 16a9 9 0 0 1 18 0z" fill="url(#icon-fill)"/><rect x="0" y="17" width="22" height="2" fill="#1c0303"/><rect x="9" y="4" width="4" height="2" fill="#1c0303"/></svg>Concierge</div>
  <div class="tile" style="left:486px;top:199px"><svg viewBox="0 0 22 20" fill="none" stroke="#1c0303" stroke-width="1.5"><path d="M1 5V1h4M17 1h4v4M21 15v4h-4M5 19H1v-4"/></svg>Barcode</div>
  <div class="tile" style="left:562px;top:199px"><svg viewBox="0 0 22 20"><path d="M11 0l11 9h-3v11H3V9H0z" fill="url(#icon-fill)"/><circle cx="11" cy="12" r="4.5" fill="#fff"/><path d="M11 9.5v5M8.5 12h5" stroke="#1c0303" stroke-width="1.6"/></svg>My Care</div>

  <div class="round-button home">
    <div class="core">
      <svg width="18" height="16" viewBox="0 0 18 16"><path d="M9 0l9 8h-2.5v8H11v-5H7v5H2.5V8H0z" fill="#c4161c"/></svg>
    </div>
  </div>
</section>

<!-- Language screen -->
<section class="screen screen--language">
  <div class="backdrop-photo" role="img" aria-label="Background photo of a potted plant against a soft grey wall"></div>
  <div class="brand">Quorvix<span class="dot"></span></div>

  <div class="lang" style="left:76px;top:140px"><span class="flag flag--us"></span>English</div>
  <div class="lang" style="left:195px;top:140px"><span class="flag flag--fr"></span>French</div>
  <div class="lang" style="left:314px;top:140px"><span class="flag flag--ae"></span>Arabic</div>
  <div class="lang" style="left:433px;top:140px"><span class="flag flag--jp"></span>Japanese</div>
  <div class="lang" style="left:552px;top:140px"><span class="flag flag--it"></span>Italian</div>

  <div class="lang" style="left:76px;top:187px"><span class="flag flag--es"></span>Spanish</div>
  <div class="lang" style="left:195px;top:187px"><span class="flag flag--cn">★</span>Chinese</div>
  <div class="lang" style="left:314px;top:187px"><span class="flag flag--vn">★</span>Vietnamese</div>
  <div class="lang" style="left:433px;top:187px"><span class="flag flag--de"></span>German</div>
  <div class="lang" style="left:552px;top:187px"><span class="flag flag--in"></span>Hindi</div>

  <div class="round-button home">
    <div class="core">
      <svg width="18" height="16" viewBox="0 0 18 16"><path d="M9 0l9 8h-2.5v8H11v-5H7v5H2.5V8H0z" fill="#c4161c"/></svg>
    </div>
  </div>
</section>

</body>
</html>
```